High-End Medical Center Website Design Project

This design is part of a well thought-out project by an experienced project manager / developer. The approved wireframe is attached. Creative interpretations / suggestions based on the layout encouraged.

The design is for a new state-of-the-art medical center located in Dallas, Texas. The target audience would likely be individuals (approx. 60% female /40% male) who are the healthcare decision-makers for their families. They would likely have insurance and be inclined to seek out top-quality care.

Potential clients would choose this client over others in their industry because the medical center is physician owned, meaning it is patient-focused rather than profit-focused. The facility is brand new, featuring the latest technology. (This includes an amazing waiting room featuring WiFi and docking stations.) The physicians are hand-picked by referral only.

The look of the site should be extremely clean. We are going for a well-organized, professional look with a bit of a warm glow (interpret that however you like). Use crisp corners and the colors in the logo.

Think modern, clean with some great use of color / font.

We can get lovely photography of the medical center once construction is complete. Feel free to use an "example image" behind the Featured Area ("Physician Owned. Patient-Focused") if you like. We are open to ideas.

ONE CHANGE REQUESTED IN THE WIREFRAME:

Remove the "Connect" 1/4 page footer area and replace with a quick contact form. You may swap the "Locations" area with the form if desired. Put social media icons at the top left of the page in the top header area.

(Note: Please use social media icons that match the design rather than standard icons. We preferred not placing the icons at the top, but the client requested this. Let's not bring more attention to them than necessary.)
Updates

We're custom programming this site, so there's no need to base it on a template. Also, we would prefer not to use typical "seen everywhere" stock images.Thanks.

Industry/Entity Type

Construction

Requirements
Must have
• Follow the wireframe. This has been approved.
Nice to have
• Examples of what hover states, links or dropdowns might look like.

```html
<!DOCTYPE html>
<html lang="en">
<head>
<meta charset="utf-8">
<title>Halden Medical Center</title>
<link href="https://fonts.googleapis.com/css2?family=Roboto:wght@300;400;500;700&display=swap" rel="stylesheet">
<style>
:root{
  --blue:#0a58a8;
  --navy:#0b3a6e;
  --teal:#3aa9b8;
  --teal-light:#5ec3cf;
  --grey-bg:#f3f3f3;
  --nav-text:#7a7a7a;
  --body-text:#333;
  --white:#fff;
}
*{box-sizing:border-box;margin:0;padding:0}
html,body{width:735px;height:1200px;overflow:hidden}
body{position:relative;font-family:"Roboto",Arial,sans-serif;color:var(--body-text);background:var(--white)}
.abs{position:absolute}

/* top bar */
.topbar{left:0;top:0;width:735px;height:34px;background:var(--blue)}
.search-field{left:84px;top:10px;width:96px;height:15px;background:var(--white)}
.search-btn{left:186px;top:9px}
.social{top:6px;width:21px;height:21px;background:#2f73b8}
.call{right:83px;top:8px;color:var(--white);font-weight:700;font-size:16px;letter-spacing:.2px}

/* nav */
.nav{left:0;top:34px;width:735px;height:56px;background:var(--white)}
.brand{left:79px;top:53px;width:172px;display:flex;align-items:center;gap:5px;color:var(--blue);font-weight:700;font-size:11.5px;letter-spacing:.2px;white-space:nowrap}
.brand-mark{flex:none;width:14px;height:14px;background:var(--blue)}
.menu{left:264px;top:34px;display:flex;height:56px;font-size:8.5px;color:var(--nav-text);text-transform:uppercase}
.menu a{display:flex;align-items:center;justify-content:center;text-decoration:none;color:inherit;height:56px;white-space:nowrap}
.menu a.active{background:#ececec;color:var(--blue);border-bottom:3px solid var(--blue);padding-top:3px}
.menu .caret::after{content:"";display:inline-block;width:3px;height:3px;border-right:1px solid #999;border-bottom:1px solid #999;transform:rotate(45deg);margin-left:5px;margin-bottom:2px}
.dropdown{left:407px;top:90px;width:91px;background:var(--teal)}
.dropdown a{display:block;height:23.5px;line-height:23.5px;padding-left:4px;font-size:6.5px;color:var(--white);text-decoration:none;border-bottom:1px solid #7fd0da}
.dropdown a:first-child{background:#35a0ae}

/* hero */
.hero{left:0;top:90px;width:735px;height:276px;background:linear-gradient(90deg,#c9c3ba 0%,#e9e6e1 25%,#8f7b66 45%,#b7aca0 65%,#8c9aa3 85%,#c5c8c9 100%)}
.hero-banner{left:324px;top:202px;width:321px;height:46px;background:rgba(30,60,60,.55);color:var(--white);text-align:center}
.hero-banner h1{font-weight:300;font-size:19.5px;padding-top:6px;letter-spacing:.3px}
.hero-banner .stars{font-size:11px;letter-spacing:2px;margin-top:1px}
.hero-tile{top:252px;width:43px;height:43px;background:#1f2a30;border:1px solid #56646b;display:flex;align-items:center;justify-content:center;color:var(--white)}
.hero-arrow{top:215px;width:22px;height:22px;border-radius:50%;background:var(--white);display:flex;align-items:center;justify-content:center}
.hero-dots{left:597px;top:346px;display:flex;gap:5px;align-items:center}
.hero-dots span{width:6px;height:6px;border-radius:50%;background:var(--white)}
.hero-dots span.on{width:11px;height:11px;background:#555;border:1.5px solid var(--white)}

/* features */
.features{left:0;top:366px;width:735px;height:250px;background:var(--grey-bg)}
.features-title{left:0;top:393px;width:735px;text-align:center;color:var(--teal);font-weight:300;font-size:29px}
.feature{top:438px;width:158px;text-align:center}
.feature-ring{width:80px;height:80px;margin:0 auto;border:3px solid var(--teal);border-radius:50%;background:var(--white);display:flex;align-items:center;justify-content:center}
.feature h3{color:var(--teal);font-weight:400;font-size:14px;margin-top:3px}
.feature p{font-size:6.5px;line-height:8.4px;margin-top:4px;color:#222;letter-spacing:-.05px}

/* about */
.divider{left:466px;top:616px;width:1px;height:229px;background:#e2e2e2}
.about-photo{left:79px;top:659px;width:185px;height:126px;border:3px solid #d8dde2;background:linear-gradient(120deg,#c9a17e,#e9e3d6 45%,#7d6658 70%,#d9cbb8)}
.section-title{color:var(--teal);font-weight:400;font-size:17.5px}
.title-rule{height:1px;background:#bbb}
.about-text{left:276px;top:692px;width:185px;font-size:6.9px;line-height:8.3px;color:#222}
.readmore{left:276px;top:772px;width:62px;height:17px;background:var(--blue);color:var(--white);font-size:6.5px;display:flex;align-items:center;justify-content:center;text-decoration:none}
.quote{left:473px;top:684px;width:184px;height:88px;background:var(--blue);color:var(--white);font-size:8.4px;line-height:10.2px;padding:11px 10px}
.quote-tail{left:490px;top:771px;width:0;height:0;border-top:11px solid var(--blue);border-right:12px solid transparent}
.quote-by{left:475px;top:788px;font-size:7.5px;color:var(--blue)}
.quote-by b{font-style:italic}
.quote-by span{color:var(--teal);font-size:6px;margin-left:2px}
.quote-nav{left:474px;top:813px;display:flex;gap:2px}
.quote-nav span{width:13px;height:2px;background:var(--teal)}
.quote-nav span:first-child{background:var(--blue)}

/* footer */
.footer{left:0;top:845px;width:735px;height:327px;background:var(--navy)}
.col-title{color:var(--white);font-size:11px;font-weight:400}
.col-rule{height:1px;background:var(--teal)}
.col-rule::before{content:"";display:block;width:36px;height:2px;background:var(--white);margin-top:-1px}
.news-item{color:var(--white);font-size:6.1px;line-height:8.2px;padding:6px 0 5px;border-bottom:1px dashed #6d8db3;width:183px;letter-spacing:-.05px}
.blog-item h4{color:var(--teal-light);font-weight:400;font-size:8.6px;margin-bottom:6px}
.blog-item p{color:var(--white);font-size:6.6px;line-height:8.2px}
.blog-sep{border-bottom:1px dashed #6d8db3;margin:8px 0 8px}
.digit{top:905px;width:26px;height:40px;background:linear-gradient(#fff 50%,#e4e9ef 50%);border-radius:3px;color:var(--blue);font-weight:700;font-size:37px;text-align:center;line-height:40px}
.minutes{left:587px;top:914px;color:var(--white);font-weight:700;font-size:17px}
.wait-text{left:473px;top:976px;width:184px;color:var(--white);font-size:6.6px;line-height:8.2px}
.address{left:80px;top:1111px;color:var(--white);font-size:7.3px;line-height:9px;font-style:normal}
.map{left:197px;top:1107px;width:166px;height:51px;background:linear-gradient(135deg,#d4d4d4,#eeeeee 50%,#c8c8c8)}
.field{background:var(--white);border-radius:2px;font-size:6px;color:#888;padding:3px 5px}
.submit{left:522px;top:1131px;width:134px;height:25px;background:linear-gradient(#8edde6,#4fb8c6);color:var(--navy);font-weight:700;font-size:12.5px;display:flex;align-items:center;justify-content:center;letter-spacing:.5px}
.copyright{left:0;top:1172px;width:735px;height:28px;background:var(--blue);border-top:1px solid #3b78bd;color:var(--white);font-size:6.5px;text-align:center;line-height:27px}
</style>
</head>
<body>

<header>
  <div class="abs topbar"></div>
  <div class="abs search-field"></div>
  <svg class="abs search-btn" width="16" height="16" viewBox="0 0 16 16"><circle cx="6.5" cy="6.5" r="4.8" fill="none" stroke="#fff" stroke-width="1.8"/><line x1="10" y1="10" x2="14.5" y2="14.5" stroke="#fff" stroke-width="2"/></svg>
  <a class="abs social" style="left:215px" aria-label="Social link"></a>
  <a class="abs social" style="left:240px" aria-label="Social link"></a>
  <a class="abs social" style="left:265px" aria-label="Social link"></a>
  <div class="abs call">CALL US: (214) 380 - 5120</div>

  <div class="abs nav"></div>
  <div class="abs brand"><span class="brand-mark"></span>HALDEN MEDICAL CENTER</div>
  <nav class="abs menu">
    <a class="active" href="#" style="width:60px">Why Halden</a>
    <a href="#" style="width:74px">Phycisians</a>
    <a class="caret" href="#" style="width:76px">Specialties</a>
    <a href="#" style="width:52px">Info</a>
    <a class="caret" href="#" style="width:72px">Locations</a>
    <a href="#" style="width:56px">Contact</a>
  </nav>
  <div class="abs dropdown">
    <a href="#">Sub Menu &nbsp;Sample</a>
    <a href="#">Sub Menu &nbsp;Sample</a>
    <a href="#">Sub Menu &nbsp;Sample</a>
    <a href="#">Sub Menu &nbsp;Sample</a>
  </div>
</header>

<section>
  <div class="abs hero" role="img" aria-label="Smiling physician in a white coat with a stethoscope, in front of a softly blurred clinic interior"></div>
  <div class="abs hero-banner"><h1>Physician Owned, Patient Focused</h1><div class="stars">★★★★★★★★★★</div></div>
  <div class="abs hero-tile" style="left:410px"><svg width="26" height="26" viewBox="0 0 26 26" fill="none" stroke="#fff" stroke-width="1.6"><path d="M5 4v7a5 5 0 0 0 10 0V4"/><path d="M10 16v3a4 4 0 0 0 8 0v-3"/><circle cx="18" cy="13" r="2.5"/></svg></div>
  <div class="abs hero-tile" style="left:465px"><svg width="26" height="26" viewBox="0 0 26 26" fill="none" stroke="#fff" stroke-width="1.6"><rect x="6" y="3" width="14" height="20"/><path d="M6 3l8 3v19l-8-2z" fill="#fff"/><rect x="16" y="10" width="3" height="3" fill="#3aa9b8" stroke="none"/></svg></div>
  <div class="abs hero-tile" style="left:519px;font-size:28px;font-weight:700">?</div>
  <div class="abs hero-arrow" style="left:13px"><svg width="8" height="10" viewBox="0 0 8 10"><path d="M6 1L2 5l4 4" fill="none" stroke="#666" stroke-width="1.5"/></svg></div>
  <div class="abs hero-arrow" style="left:693px"><svg width="8" height="10" viewBox="0 0 8 10"><path d="M2 1l4 4-4 4" fill="none" stroke="#666" stroke-width="1.5"/></svg></div>
  <div class="abs hero-dots"><span class="on"></span><span></span><span></span><span class="on"></span></div>
</section>

<section>
  <div class="abs features"></div>
  <h2 class="abs features-title">What Set Us Apart</h2>
  <div class="abs feature" style="left:95px">
    <div class="feature-ring"><svg width="40" height="40" viewBox="0 0 40 40"><g transform="rotate(35 20 20)"><rect x="15" y="5" width="10" height="30" rx="5" fill="none" stroke="#111" stroke-width="2.5"/><path d="M15 20h10v10a5 5 0 0 1-10 0z" fill="#111"/></g></svg></div>
    <h3>Technology</h3>
    <p>Lorem ipsum dolor sit amet, consectetur adipiscing elit. Nullam ullamcorper orci sit amet velit laoreet varius. Suspendisse sit amet mattis dolor, vel condimentum justo. Ut eu eros iaculis, blandit massa at, commodo justo. Aliquam erat volutpat. Praesent</p>
  </div>
  <div class="abs feature" style="left:290px">
    <div class="feature-ring"><svg width="40" height="40" viewBox="0 0 40 40" fill="none" stroke="#111" stroke-width="2.5"><rect x="6" y="12" width="28" height="21" rx="3"/><path d="M15 12V8h10v4"/><path d="M20 17v11M14.5 22.5h11" stroke-width="3"/></svg></div>
    <h3>Quality of Care</h3>
    <p>Lorem ipsum dolor sit amet, consectetur adipiscing elit. Nullam ullamcorper orci sit amet velit laoreet varius. Suspendisse sit amet mattis dolor, vel condimentum justo. Ut eu eros iaculis, blandit massa at, commodo justo. Aliquam erat volutpat. Praesent</p>
  </div>
  <div class="abs feature" style="left:487px">
    <div class="feature-ring"><svg width="40" height="40" viewBox="0 0 40 40" fill="none" stroke="#111" stroke-width="2"><line x1="20" y1="6" x2="20" y2="36" stroke-width="2.5"/><path d="M6 12q7-3 14 2q7-5 14-2"/><path d="M15 18q10 3 0 7q10 3 0 7M25 18q-10 3 0 7q-10 3 0 7"/></svg></div>
    <h3>Patient Experience</h3>
    <p>Lorem ipsum dolor sit amet, consectetur adipiscing elit. Nullam ullamcorper orci sit amet velit laoreet varius. Suspendisse sit amet mattis dolor, vel condimentum justo. Ut eu eros iaculis, blandit massa at, commodo justo. Aliquam erat volutpat. Praesent</p>
  </div>
</section>

<section>
  <div class="abs divider"></div>
  <div class="abs about-photo" role="img" aria-label="Doctor listening to a patient's heartbeat with a stethoscope"></div>
  <h2 class="abs section-title" style="left:276px;top:657px">Headings</h2>
  <div class="abs title-rule" style="left:276px;top:680px;width:184px"></div>
  <p class="abs about-text">Lorem ipsum dolor sit amet, consectetur adipiscing elit. Nullam ullamcorper orci sit amet velit laoreet varius. Suspendisse sit amet mattis dolor, vel condimentum justo. Ut eu eros iaculis, blandit massa at, commodo justo. Aliquam erat volutpat. Praesent mollis dolor nunc, non pellentesque nulla sagittis vitae. Suspendisse vel adipiscing velit. Proin fermentum luctus ultricies. Phasellus quam odio, sodales eu lorem ut, tempor laoreet dolor. Vestibulum vitae est ac augue tincidunt ornare ac eu enim.</p>
  <a class="abs readmore" href="#">readmore</a>

  <h2 class="abs section-title" style="left:474px;top:657px">Testimonials</h2>
  <blockquote class="abs quote">Donec dictum sodales ligula vel varius. Aenean eget magna sed nunc posuere fringilla. In tincidunt, turpis at tempor porta, massa odio vestibulum ante, vitae rutrum ligula ipsum sed lorem. Sed sapien felis, venenatis ac rutrum nec, faucibus quis</blockquote>
  <div class="abs quote-tail"></div>
  <div class="abs quote-by"><b>Marcus,</b><span>CEO KVRL</span></div>
  <div class="abs quote-nav"><span></span><span></span><span></span></div>
</section>

<footer>
  <div class="abs footer"></div>

  <h3 class="abs col-title" style="left:83px;top:863px">News</h3>
  <div class="abs col-rule" style="left:81px;top:880px;width:183px"></div>
  <div class="abs" style="left:81px;top:893px">
    <p class="news-item">Lorem ipsum dolor sit amet, consectetur adipiscing elit. Nullam ullamcorper orci sit amet velit laoreet varius. Suspendisse sit</p>
    <p class="news-item">Lorem ipsum dolor sit amet, consectetur adipiscing elit. Nullam ullamcorper orci sit amet velit laoreet varius. Suspendisse sit</p>
    <p class="news-item">Lorem ipsum dolor sit amet, consectetur adipiscing elit. Nullam ullamcorper orci sit amet velit laoreet varius. Suspendisse sit</p>
    <p class="news-item">Lorem ipsum dolor sit amet, consectetur adipiscing elit. Nullam ullamcorper orci sit amet velit laoreet varius. Suspendisse sit</p>
  </div>

  <h3 class="abs col-title" style="left:278px;top:863px">Blog</h3>
  <div class="abs col-rule" style="left:276px;top:880px;width:183px"></div>
  <div class="abs" style="left:278px;top:900px;width:181px">
    <div class="blog-item"><h4>Lorem ipsum dolor sit amet, consectetur</h4><p>Nullam ullamcorper orci sit amet velit laoreet varius. Suspendisse sit amet mattis dolor, vel condimentum justo. Ut eu eros iaculis, blandit massa at, commodo justo. Aliquam</p></div>
    <div class="blog-sep"></div>
    <div class="blog-item"><h4>Lorem ipsum dolor sit amet, consectetur</h4><p>Nullam ullamcorper orci sit amet velit laoreet varius. Suspendisse sit amet mattis dolor, vel condimentum justo. Ut eu eros iaculis, blandit massa at, commodo justo. Aliquam</p></div>
  </div>

  <h3 class="abs col-title" style="left:474px;top:863px">Averange wait time</h3>
  <div class="abs col-rule" style="left:473px;top:880px;width:183px"></div>
  <svg class="abs" style="left:476px;top:907px" width="37" height="37" viewBox="0 0 37 37"><circle cx="18.5" cy="18.5" r="16" fill="none" stroke="#fff" stroke-width="3"/><circle cx="18.5" cy="18.5" r="11" fill="#2f6aa8"/><path d="M18.5 10v9l6 4" fill="none" stroke="#fff" stroke-width="2.2"/></svg>
  <div class="abs digit" style="left:525px">0</div>
  <div class="abs digit" style="left:555px">8</div>
  <div class="abs minutes">minutes</div>
  <p class="abs wait-text">Lorem ipsum dolor sit amet, consectetur adipiscing elit. Nullam ullamcorper orci sit amet velit laoreet varius. Suspendisse sit amet mattis dolor, vel condimentum justo. Ut eu eros iaculis, blandit massa at, commodo justo. Aliquam</p>

  <h3 class="abs col-title" style="left:81px;top:1047px">Location</h3>
  <div class="abs col-rule" style="left:80px;top:1062px;width:282px"></div>
  <div class="abs brand" style="top:1078px;left:80px;color:#fff"><span class="brand-mark" style="background:#fff"></span>HALDEN MEDICAL CENTER</div>
  <address class="abs address"><b>Halden Medical Center</b><br>2450 Linden Park Way Suite B<br>Riverton, Texas 75010<br>Phone: (469) 555-0142<br>Fax: (469) 555-0143</address>
  <div class="abs map" role="img" aria-label="Street map showing the center's location"></div>

  <h3 class="abs col-title" style="left:379px;top:1047px">Contact</h3>
  <div class="abs col-rule" style="left:376px;top:1062px;width:280px"></div>
  <div class="abs field" style="left:375px;top:1079px;width:134px;height:15px">Name</div>
  <div class="abs field" style="left:522px;top:1079px;width:134px;height:15px">Email</div>
  <div class="abs field" style="left:375px;top:1104px;width:134px;height:54px">Message</div>
  <div class="abs field" style="left:522px;top:1104px;width:134px;height:16px">Telp</div>
  <div class="abs submit">SUBMIT</div>

  <div class="abs copyright">Copyright © 2013. All rights reserved. Terms and Condition | Privacy | Sitemap</div>
</footer>

</body>
</html>
```